Financing company needs a 1-page website with contact form

We are a financing company focusing on manufacturing sector. We need a simple 1 page website with contact form that is consistent and aligned to the main website (it is part of a bigger company). Please adhere to the same color scheme to make it look similar, but not necessarily a carbon copy.

Website link www.orvalcapital.net

I also need the designer to suggest stock images that are suitable (related to manufacturing sector).

Files to be in html format.

Font: Try to match the main website or use a simple, sans serif font that is similar

Reason: Dear designers, thank you for your submissions. I believe I have given my feedback to all of you. But we would like to extend it by a few days to give a chance for more designers to join, and tweak the existing submissions. Thanks!

Target Market(s)

Small and medium companies in manufacturing sector, potential investors

Industry/Entity Type

Financial Service

Font styles to use
Sans Serif

Requirements
Must have
• Consistency to the main website www.orvalcapital.net
• Can use simialr layout too to make it easier
• Contact form
• to have a one page website like this example https://www.trylumo.com/

```html
<!DOCTYPE html>
<html lang="en">
<head>
<meta charset="utf-8">
<title>Orval Meridian Factoring</title>
<link rel="stylesheet" href="https://fonts.googleapis.com/css2?family=Arimo:wght@400;700&display=swap">
<style>
:root{
  --red:#b01e23;
  --red-dark:#9a171c;
  --light:#ececec;
  --ink:#111111;
  --muted:#555555;
  --white:#ffffff;
  --field:#f3e4e4;
}
*{box-sizing:border-box;margin:0;padding:0}
html,body{width:1200px;height:2490px;overflow:hidden}
body{font-family:"Arimo",Arial,sans-serif;color:var(--ink);background:var(--white);position:relative}

/* Hero */
.hero{position:absolute;left:0;top:0;width:1200px;height:652px;overflow:hidden}
.hero-photo{position:absolute;inset:0;background:
  linear-gradient(180deg,rgba(255,255,255,.85) 0%,rgba(230,230,230,.35) 16%,rgba(0,0,0,0) 30%),
  linear-gradient(90deg,#b59a3a 0%,#8d7c52 22%,#9a9ea4 45%,#7b8896 65%,#4f5966 100%)}
.hero-shade{position:absolute;inset:0;background:linear-gradient(180deg,rgba(0,0,0,0) 45%,rgba(0,0,0,.35) 100%)}
.nav{position:absolute;left:0;top:0;width:1200px;height:150px}
.brand{position:absolute;left:38px;top:55px;display:flex;align-items:center;gap:12px;font-size:36px;font-weight:400;color:#3a3a3a;letter-spacing:1px}
.brand-mark{width:26px;height:26px;background:var(--red)}
.menu{position:absolute;right:92px;top:62px;display:flex;gap:26px;align-items:center;font-size:15px;color:#222}
.menu-toggle{width:28px;height:28px;border:2px solid #555;display:flex;flex-direction:column;justify-content:center;gap:4px;padding:0 5px}
.menu-toggle span{display:block;height:2px;background:#555}
.hero-dots{position:absolute;left:540px;top:305px}
.hero-title{position:absolute;left:0;top:350px;width:1200px;text-align:center;color:var(--white);font-size:50px;line-height:62px;font-weight:400}
.btn{display:inline-block;background:var(--red);color:var(--white);font-size:20px;text-align:center}
.hero .btn{position:absolute;left:508px;top:515px;width:182px;height:46px;line-height:46px}

/* Who */
.who{position:absolute;left:0;top:652px;width:1200px;height:348px;background:var(--light);text-align:center}
.who-icon{position:absolute;left:555px;top:45px}
.section-title{font-size:58px;font-weight:400;color:var(--ink)}
.who .section-title{position:absolute;left:0;top:135px;width:1200px}
.stars{position:absolute;left:0;width:1200px;text-align:center;font-size:14px;letter-spacing:4px;color:var(--ink)}
.who .stars{top:212px}
.who-text{position:absolute;left:80px;top:240px;width:1040px;font-size:16px;line-height:23px}

/* Services */
.services{position:absolute;left:0;top:1000px;width:1200px;height:420px;background:var(--red);color:var(--white)}
.services-photo{position:absolute;left:92px;top:58px;width:451px;height:304px;background:linear-gradient(180deg,#c9cdd3 0%,#8a9aa8 40%,#2f3c48 72%,#495560 100%);box-shadow:4px 6px 10px rgba(0,0,0,.35)}
.services h2{position:absolute;left:615px;top:62px;font-size:50px;font-weight:400}
.services p{position:absolute;left:615px;top:132px;width:500px;font-size:15px;line-height:23px;text-align:justify;color:#f7dede}
.services .btn{position:absolute;left:615px;top:310px;width:145px;height:42px;line-height:42px;background:var(--white);color:var(--red);font-size:18px}

/* People */
.people{position:absolute;left:0;top:1420px;width:1200px;height:555px;background:var(--light)}
.people .section-title{position:absolute;left:0;top:60px;width:1200px;text-align:center}
.people .stars{top:138px}
.people-intro{position:absolute;left:80px;top:160px;width:1040px;text-align:center;font-size:16px;line-height:24px}
.focus{position:absolute;left:0;width:1200px;display:flex;justify-content:center;gap:60px;font-size:15px}
.focus li{list-style:none}
.focus li::before{content:"";display:inline-block;width:7px;height:7px;background:#666;border-radius:50%;margin-right:10px;vertical-align:middle}
.focus-a{top:224px}
.focus-b{top:266px}
.timeline{position:absolute;left:190px;top:328px}
.person{position:absolute;top:362px;width:280px;text-align:center}
.person h3{font-size:21px;font-weight:400}
.person .role{font-size:15px;color:var(--muted);margin-top:5px}
.person p{font-size:12px;line-height:16px;margin-top:9px;text-align:justify;text-align-last:center}

/* Contact */
.contact{position:absolute;left:0;top:1975px;width:1200px;height:490px;background:var(--red);color:var(--white)}
.contact h2{position:absolute;font-size:50px;font-weight:400;padding-bottom:8px;border-bottom:3px dashed var(--white)}
.contact .left h2{left:92px;top:50px}
.contact .right h2{left:715px;top:50px}
.office{position:absolute;left:92px;font-size:15px;line-height:21px}
.tag{display:inline-block;background:var(--white);color:var(--red);font-weight:700;font-size:15px;padding:3px 10px;margin-bottom:8px}
.office-tr{top:140px}
.office-hk{top:290px}
.label{display:flex;align-items:center;gap:6px}
.form{position:absolute;left:715px;top:145px;width:383px}
.field{background:var(--field);color:#c78a8c;font-size:15px;padding:0 10px;height:40px;line-height:40px;margin-bottom:12px}
.field b{color:var(--red);font-weight:400}
.row{display:flex;gap:12px}
.row .field{flex:1}
.field.area{height:122px;line-height:22px;padding-top:8px}
.note{font-size:15px;margin-top:12px}
.submit{display:block;width:145px;height:40px;line-height:40px;background:var(--field);color:#c78a8c;text-align:center;font-size:15px;margin-top:20px}

.footer{position:absolute;left:92px;top:2471px;font-size:13px}
</style>
</head>
<body>

<header class="hero">
  <div class="hero-photo" role="img" aria-label="Photo of an offshore industrial platform with yellow cranes and pipework over the sea"></div>
  <div class="hero-shade"></div>
  <nav class="nav">
    <div class="brand"><span class="brand-mark"></span>ORVAL MERIDIAN</div>
    <div class="menu">
      <span>Who Are We?</span><span>Our Services</span><span>Key Personnel</span><span>Contact us</span>
      <span class="menu-toggle"><span></span><span></span><span></span></span>
    </div>
  </nav>
  <svg class="hero-dots" width="120" height="30" viewBox="0 0 120 30" aria-hidden="true">
    <line x1="10" y1="15" x2="110" y2="15" stroke="#b01e23" stroke-width="4"/>
    <circle cx="15" cy="15" r="10" fill="#fff" stroke="#b01e23" stroke-width="5"/>
    <circle cx="60" cy="15" r="10" fill="#fff" stroke="#b01e23" stroke-width="5"/>
    <circle cx="105" cy="15" r="10" fill="#fff" stroke="#b01e23" stroke-width="5"/>
  </svg>
  <h1 class="hero-title">Nurturing Partnerships to Drive Real<br>Economy Growth</h1>
  <a class="btn">Learn More</a>
</header>

<section class="who">
  <svg class="who-icon" width="90" height="90" viewBox="0 0 90 90" aria-hidden="true">
    <circle cx="45" cy="45" r="42" fill="none" stroke="#b01e23" stroke-width="3"/>
    <circle cx="45" cy="45" r="34" fill="#b01e23"/>
    <circle cx="45" cy="36" r="10" fill="#fff"/>
    <path d="M27 64c2-11 9-16 18-16s16 5 18 16z" fill="#fff"/>
  </svg>
  <h2 class="section-title">Who Are We?</h2>
  <div class="stars">★★★★</div>
  <p class="who-text">Orval Meridian Factoring is a specialist financier focusing on small and medium-sized enterprises (SMEs) in emerging markets. We provide working capital, typically in structured trade finance, to businesses in the manufacturing and retail sectors.<br>We are supported by a team of highly experienced professionals with in-depth knowledge of credit, private equity and investments.</p>
</section>

<section class="services">
  <div class="services-photo" role="img" aria-label="Photo of a large cargo ship moored at an industrial harbour"></div>
  <h2>Our Services</h2>
  <p>Our key focus is on companies in the manufacturing sector that are in need of working capital. We meet their financing needs by developing structured offerings after a careful analysis of the companies' operations and processes. Our business model is based on structured lending in the form of trade finance facilities. How we are different is the way we combine a best practices mezzanine discipline with our experience in trade finance structuring.</p>
  <a class="btn">Learn More</a>
</section>

<section class="people">
  <h2 class="section-title">Key Personnel</h2>
  <div class="stars">★★★★</div>
  <p class="people-intro">Our team comprises of seasoned professionals from leading investment and commercial banks, trading and accounting firms. They have significant experience working in various tenures in restructuring, financing and other investments, with a proven track record in:</p>
  <ul class="focus focus-a">
    <li>Private equity &amp; mezzanine deals</li>
    <li>Islamic financing structures</li>
    <li>SME credits, factoring and leasing</li>
  </ul>
  <ul class="focus focus-b">
    <li>Turnaround structuring, debt and cash collection</li>
    <li>SME management and advisory</li>
  </ul>
  <svg class="timeline" width="820" height="12" viewBox="0 0 820 12" aria-hidden="true">
    <line x1="0" y1="6" x2="820" y2="6" stroke="#b01e23" stroke-width="2"/>
    <circle cx="80" cy="6" r="5" fill="#b01e23"/>
    <circle cx="410" cy="6" r="5" fill="#b01e23"/>
    <circle cx="740" cy="6" r="5" fill="#b01e23"/>
  </svg>
  <div class="person" style="left:130px">
    <h3>Selim Arduç</h3>
    <div class="role">Managing Partner</div>
    <p>Selim Arduç's expertise spans from investment banking, especially focused on private equity, to project finance and special situations. He also has in-depth knowledge of Turkish debt and equity capital markets.</p>
  </div>
  <div class="person" style="left:460px">
    <h3>Kerem Tolan</h3>
    <div class="role">Managing Partner</div>
    <p>Kerem Tolan has significant experience in special situations, deal structuring and due diligence. Prior to Orval Meridian Factoring, he was at NVR Investments, a multi-billion, multi-strategy hedge fund.</p>
  </div>
  <div class="person" style="left:790px">
    <h3>Dorin Valescu</h3>
    <div class="role">Manager</div>
    <p>Dorin Valescu is responsible for overseeing origination and portfolio management. He has close to 10 years of experience in trade finance, structured finance and commodity trading.</p>
  </div>
</section>

<section class="contact">
  <div class="left">
    <h2>Contact Us</h2>
    <div class="office office-tr">
      <span class="tag">Turkey</span>
      <div class="label"><svg width="13" height="13" viewBox="0 0 14 14" aria-hidden="true"><path d="M1 7 7 1l6 6v6H9V9H5v4H1z" fill="#fff"/></svg><b>Address:</b></div>
      <div>Lale Residence D 12, Cinar Cd No 48 Levent, Istanbul</div>
      <div class="label"><svg width="13" height="13" viewBox="0 0 14 14" aria-hidden="true"><path d="M3 1h3l1 3-2 1.5a8 8 0 0 0 3.5 3.5L10 7l3 1v3c0 1-1 2-2 2C6 13 1 8 1 3c0-1 1-2 2-2z" fill="#fff"/></svg><b>Phone:</b></div>
      <div>+90 212 555 01 37</div>
    </div>
    <div class="office office-hk">
      <span class="tag">Hong Kong</span>
      <div class="label"><svg width="13" height="13" viewBox="0 0 14 14" aria-hidden="true"><path d="M1 7 7 1l6 6v6H9V9H5v4H1z" fill="#fff"/></svg><b>Address:</b></div>
      <div>Room 214, 2/F., Harbour Trade Building</div>
      <div>8-10 Lotus Lane, Kwai Chung, N.T., Hong Kong</div>
    </div>
  </div>
  <div class="right">
    <h2>Send A Message</h2>
    <div class="form">
      <div class="field">Name<b>*</b>:</div>
      <div class="row">
        <div class="field">Email<b>*</b>:</div>
        <div class="field">Phone/ Mobile:</div>
      </div>
      <div class="field area">Comments/ Message:</div>
      <div class="note">*Mandatory fields</div>
      <span class="submit">Submit</span>
    </div>
  </div>
</section>

<footer class="footer">Copyright © 2015 Orval Meridian Factoring. All rights reserved.</footer>

</body>
</html>
```